Online Art Gallery & Art Management Firm looking for a business card

I'm launching an online art gallery (paintings, photography, drawings, furniture, books, ...) where people can buy all types of art. It's a platform where young and unknown artists can showcase their oeuvre.

Additionally, the venture will act as my advising company for artists. I help them out with their business side of life and become their representative.

The company name: The Velvet Parlour
Logo is attached

I'm looking for something very classy and upmarket.
Updates

Reason: Logo wasn't finished yet...

The design should include the following information: - Name: Pieter Vandomme - Title: Founder - Mobile: +32 (0) 486 514 362 - E-mail: pieter@velvet-parlour.example - Website www.velvet-parlour.example I prefer the have the logo (without website) on the one side and the information on the other. Best regards Pieter

Target Market(s)

Art buyers / art dealers / artists / middle class / upmarket /

Industry/Entity Type

Artists

Colors

Designer to choose colors to be used in the design.

Requirements
Must have
• Must communicate credibility, trust and integrity
Nice to have
• Something classy, chique
Should not have
• Nothing to artistic or creative

```html
<!DOCTYPE html>
<html lang="en">
<head>
<meta charset="utf-8">
<title>The Velvet Parlour — Business Card</title>
<link rel="stylesheet" href="https://fonts.googleapis.com/css2?family=Poiret+One&family=Oswald:wght@400;500&family=Open+Sans:wght@400&display=swap">
<style>
  :root {
    --backdrop: #d9d8d8;
    --paper: #ffffff;
    --ink: #0b0b0b;
    --ink-soft: #2a2a2a;
    --reverse: #f2f2f2;
  }
  * { box-sizing: border-box; margin: 0; padding: 0; }
  html, body { width: 1200px; height: 900px; overflow: hidden; }
  body {
    background: var(--backdrop);
    display: flex;
    flex-direction: column;
    align-items: center;
    justify-content: center;
    gap: 50px;
  }
  .card {
    position: relative;
    width: 560px;
    height: 320px;
    box-shadow: 0 6px 18px rgba(0,0,0,0.18);
  }
  .card--front { background: var(--paper); color: var(--ink); }
  .card--back {
    background: var(--ink);
    display: flex;
    align-items: center;
    justify-content: center;
  }
  .brand {
    font-family: "Poiret One", sans-serif;
    text-transform: uppercase;
    letter-spacing: 0.32em;
  }
  .card--front .brand {
    position: absolute;
    left: 40px;
    top: 40px;
    font-size: 15px;
    color: var(--ink-soft);
  }
  .card--back .brand {
    font-size: 28px;
    color: var(--reverse);
  }
  .name-band {
    position: absolute;
    left: 0;
    top: 84px;
    width: 100%;
    height: 96px;
    background: var(--ink);
    padding: 10px 40px;
    display: flex;
    flex-direction: column;
    justify-content: center;
  }
  .name-band .name {
    font-family: "Oswald", sans-serif;
    font-weight: 500;
    text-transform: uppercase;
    font-size: 36px;
    line-height: 1;
    letter-spacing: 0.02em;
    color: var(--paper);
  }
  .role {
    position: absolute;
    left: 40px;
    top: 194px;
    font-family: "Open Sans", sans-serif;
    font-size: 17px;
    color: var(--ink);
  }
  .contact-list {
    position: absolute;
    left: 40px;
    bottom: 28px;
    list-style: none;
    font-family: "Open Sans", sans-serif;
    font-size: 11px;
    color: var(--ink);
  }
  .contact-list li {
    display: flex;
    align-items: center;
    gap: 6px;
    line-height: 20px;
  }
  .contact-list svg { width: 11px; height: 11px; flex: none; }
</style>
</head>
<body>
  <section class="card card--front" aria-label="Card front">
    <p class="brand">The Velvet Parlour</p>
    <div class="name-band">
      <span class="name">Pieter</span>
      <span class="name">Vandomme</span>
    </div>
    <p class="role">Founder</p>
    <ul class="contact-list">
      <li>+32 (0) 486 514 362
        <svg viewBox="0 0 12 12" aria-hidden="true"><path fill="#0b0b0b" d="M3 1h2l1 3-1.5 1a6 6 0 0 0 2.5 2.5L8 6l3 1v2a1 1 0 0 1-1 1A9 9 0 0 1 2 2a1 1 0 0 1 1-1z"/></svg>
      </li>
      <li>pieter@velvet-parlour.example
        <svg viewBox="0 0 12 12" aria-hidden="true"><rect x="1" y="2.5" width="10" height="7" rx="1" fill="none" stroke="#0b0b0b" stroke-width="1.2"/><path d="M1.5 3l4.5 3.5L10.5 3" fill="none" stroke="#0b0b0b" stroke-width="1.2"/></svg>
      </li>
      <li>www.velvet-parlour.example
        <svg viewBox="0 0 12 12" aria-hidden="true"><circle cx="6" cy="6" r="5" fill="#0b0b0b"/><path d="M1 6h10M6 1c-2 2.5-2 7.5 0 10M6 1c2 2.5 2 7.5 0 10" fill="none" stroke="#fff" stroke-width="0.8"/></svg>
      </li>
    </ul>
  </section>

  <section class="card card--back" aria-label="Card back">
    <p class="brand">The Velvet Parlour</p>
  </section>
</body>
</html>
```